Washington DC Solo Practitioner Law Firm needs Stationery and Business Card Design

We need a letterhead and business card for a new law firm based in Washington DC called Marlowe PLLC. The law firm is a single lawyer practicing appellate law (U.S. Supreme Court, Federal District Courts, State Supreme Courts).
We already have a logo designed through a PixelBazaar contest. The letterhead and the business card should include the Logo and have the same look and feel as the Logo - same fonts and colors, please. We would like a clean, crisp, simple, professional look. The design should convey stability and experience.
We have .png and .psd and .ai files for the logo, as needed
Dark blue color is PANTONE P 108-16 C
Grey color is PANTONE P 179-11 C
Type face is Century Gothic Regular typeface

```html
<!DOCTYPE html>
<html lang="en">
<head>
<meta charset="utf-8">
<title>Marlowe PLLC — Business Card</title>
<link href="https://fonts.googleapis.com/css2?family=Didact+Gothic&display=swap" rel="stylesheet">
<style>
  :root {
    --navy: #0d3a5c;
    --navy-line: #1d4a6c;
    --card-grey: #e6e6e6;
    --ink-grey: #5d5d5d;
    --backdrop: #d9d6d1;
    --white: #ffffff;
  }
  * { margin: 0; padding: 0; box-sizing: border-box; }
  html, body {
    width: 1200px; height: 900px; overflow: hidden;
    background: var(--backdrop);
    font-family: "Didact Gothic", "Century Gothic", sans-serif;
  }
  .sheet {
    position: relative; width: 1200px; height: 900px;
  }
  .card {
    position: absolute;
    width: 560px; height: 320px;
    box-shadow: 0 6px 18px rgba(0,0,0,0.18);
  }
  /* front */
  .card-front {
    left: 80px; top: 110px;
    background: var(--navy);
    color: var(--white);
  }
  .card-front .brand {
    position: absolute; left: 0; right: 0; top: 112px;
    display: flex; flex-direction: column; align-items: center;
  }
  .brand-row { display: flex; align-items: center; gap: 18px; }
  .brand-square { width: 30px; height: 30px; background: currentColor; }
  .brand-name {
    font-size: 34px; letter-spacing: 3px; line-height: 1;
  }
  .brand-tagline {
    margin-top: 14px; font-size: 10px; letter-spacing: 1.5px;
  }
  /* back */
  .card-back {
    left: 560px; top: 470px;
    background: var(--card-grey);
    color: var(--ink-grey);
  }
  .card-back .brand {
    position: absolute; left: 40px; top: 44px;
    color: var(--navy);
  }
  .card-back .brand-name { font-size: 30px; }
  .card-back .brand-tagline { color: var(--ink-grey); margin-left: 48px; }
  .divider {
    position: absolute; left: 40px; right: 40px; top: 196px;
    height: 1px; background: var(--navy-line);
  }
  .person {
    position: absolute; left: 40px; top: 160px;
    font-size: 24px; color: var(--ink-grey);
  }
  .office {
    position: absolute; right: 40px; top: 134px;
    text-align: right; font-size: 12px; line-height: 1.4;
  }
  .office strong { font-weight: normal; color: var(--navy); }
  .contact {
    position: absolute; left: 40px; top: 212px;
    font-size: 14px; line-height: 1.55;
    display: grid; grid-template-columns: 58px auto;
  }
</style>
</head>
<body>
<main class="sheet">
  <section class="card card-front" aria-label="Business card front">
    <div class="brand">
      <div class="brand-row">
        <span class="brand-square"></span>
        <span class="brand-name">MARLOWE PLLC</span>
      </div>
      <p class="brand-tagline">TRIAL AND APPELLATE LITIGATION</p>
    </div>
  </section>

  <section class="card card-back" aria-label="Business card back">
    <div class="brand">
      <div class="brand-row">
        <span class="brand-square"></span>
        <span class="brand-name">MARLOWE PLLC</span>
      </div>
      <p class="brand-tagline">TRIAL AND APPELLATE LITIGATION</p>
    </div>
    <p class="person">Evan Marlowe</p>
    <address class="office">
      <strong>MarlowePLLC</strong><br>
      1400 L Street NW, Suite 210<br>
      Washington, DC 20005
    </address>
    <div class="divider"></div>
    <div class="contact">
      <span>Phone</span><span>202-555-0148</span>
      <span>Fax</span><span>571-555-0193</span>
      <span>Email</span><span>emarlowe@marlowepllc.com</span>
    </div>
  </section>
</main>
</body>
</html>
```